Harbor Motor Website

We need a Wordpress site designed for a local automotive repair facility. Our goals for the website are the following:
-"Humanize" the business by showing our people and location (building).
-Communicate our "Local / Community" orientation (not a national chain store)
-Above the fold call to action(s). Online Appointment Schedule, Loaner Car Reservation and Chat Feature.
-Business Strengthening by showing industry affiliations.
Our corporate colors are: Blue Pantone 293 and Light Grey 427. Accent colors are Yellow Pantone 123 and Lime Green (lots of colors i know)
We have been trying to develop a site similar to this site: www.brightlanegarage.com. I like the header image(s). I believe this site reinforces local ownership and conveys trust.
We built this site to try and duplicate but I do not like the results:
http://pelvistudio.com/harbor2/
This is our current site: www.harbormotorrepairplace.com
My SEO firm would like you to adhere to the following:
Here are the basics:
+ Full width of site 1080px, centered
+ Header no taller than 300px
+ Need standard selection of pages, including a full page layout
+ On pages with a sidebar, main column width at least 640px, sidebar 320px
+ All page titles should be an H1, and the only H1 on the page
+ Provide 4 footer widgets spanning the width of the site
Images are uploaded. Please let me know if there are additional images or direction needed.
Thanks,
Martin Kovacs
I have made committed on the payment for this project. I am looking forward to seeing some great WordPress designs.
Thank you,
Martin
I have uploaded an image of a Postcard that we send out in our local area. Many of our print materials carry this type of look and feel.
I HESITATED to upload this because I do not want to "stifle" or "steer" your creativity. I thought you may be able to pull some elements out of this for consistency. It is alright if you choose a different direction with your graphic elements.
Thanks,
Martin
First off, thanks for all the great work. Make sure you get your final ideas uploaded by the deadline (tomorrow).
I will take a few days to review, get feedback from my colleges and then make a final selection.
Your hard work is appreciated.
Sincerely,
Martin
Target Market(s)
35-60 years old with an even mix of male and female.
Upper income demographic who are driving 2+ vehicles in the household that are 3 years or older.
Industry/Entity Type
Automotive
Look and feel

```html
<!DOCTYPE html>
<html lang="en">
<head>
<meta charset="utf-8">
<title>Harbor Motor Repair in Tempe</title>
<link href="https://fonts.googleapis.com/css2?family=Open+Sans:wght@400;600;700&family=Raleway:wght@300;400;500;600&display=swap" rel="stylesheet">
<style>
:root{
  --night:#0c0f2e;
  --night-2:#1a1f4a;
  --blue:#2b7bd3;
  --blue-deep:#1c5ec6;
  --lime:#7fbb1c;
  --lime-soft:#8cc63f;
  --orange:#f39a1e;
  --orange-dark:#e58312;
  --red:#e0281a;
  --ink:#333;
  --muted:#666;
  --line:#dcdcdc;
  --panel:#ececec;
  --footer:#2c3444;
  --footer-text:#9aa3b2;
  --white:#fff;
}
*{box-sizing:border-box;margin:0;padding:0}
html,body{width:1200px;height:2840px;overflow:hidden}
body{
  background:linear-gradient(180deg,#3a2a25 0,var(--night-2) 200px,var(--night) 700px,var(--night) 100%);
  font-family:"Open Sans",Arial,sans-serif;color:var(--ink);font-size:13px;position:relative;
}
.page{position:absolute;left:130px;top:0;width:940px}

/* header */
.site-header{position:relative;height:222px}
.header-photo{position:absolute;left:0;top:0;width:940px;height:222px;
  background:linear-gradient(180deg,#6a4a3a 0,#8a5a3a 40%,#3c3a44 75%,#2a2c3a 100%)}
.owner-photo{position:absolute;left:0;top:40px;width:120px;height:182px;
  background:linear-gradient(180deg,#7a7f8a,#c9cfd8)}
.brand{position:absolute;left:368px;top:36px;background:var(--blue-deep);color:var(--white);
  font-family:"Open Sans",sans-serif;font-weight:700;font-size:20px;padding:6px 16px;display:flex;align-items:center;gap:8px}
.brand .dot{width:12px;height:12px;background:var(--orange)}
.hours-card{position:absolute;left:150px;top:118px;background:rgba(255,255,255,.9);padding:10px 14px;font-size:12px;line-height:19px;color:#222}
.hours-card p{display:flex;align-items:center;gap:6px}
.call{position:absolute;right:0;top:10px;color:var(--white);text-align:left;width:170px}
.call small{font-size:13px;display:block}
.call strong{font-size:25px;font-weight:600;letter-spacing:.5px}
.years-seal{position:absolute;right:26px;top:92px;width:110px;height:110px;border-radius:50%;
  background:radial-gradient(circle,#2a5bb0 50%,#d7a83a 52%,#d7a83a 100%)}

/* nav */
.main-nav{margin-top:10px;background:var(--white);height:66px;display:flex;align-items:center;padding:0 14px;border-bottom:1px solid var(--line)}
.main-nav a{font-size:12px;font-weight:600;color:#333;text-decoration:none;padding:14px 12px;border:1px solid var(--line);margin-right:-1px;background:#f5f5f5;white-space:nowrap}
.main-nav a.current{background:var(--white)}

.content{background:var(--white);padding:6px 14px 0}

/* slider */
.hero{position:relative;height:348px;background:linear-gradient(110deg,#1f3e7a 0,#4d6ea3 35%,#8ea2bd 60%,#2c3950 100%)}
.hero-caption{position:absolute;left:20px;top:208px;color:var(--white)}
.hero-caption h2{font-family:"Raleway",sans-serif;font-weight:600;font-size:30px;text-shadow:0 1px 3px rgba(0,0,0,.5)}
.hero-caption p{font-family:"Raleway",sans-serif;font-size:20px;line-height:28px;margin-top:4px;text-shadow:0 1px 3px rgba(0,0,0,.5)}
.hero-dots{position:absolute;left:435px;bottom:10px;display:flex;gap:6px}
.hero-dots i{width:7px;height:7px;border-radius:50%;background:rgba(255,255,255,.6)}
.hero-dots i:first-child{background:var(--white)}

/* welcome */
.welcome h1{font-family:"Raleway",sans-serif;font-weight:300;font-size:31px;line-height:34px;color:#555;margin:30px 0 0}
.welcome h1 span{display:block;color:var(--blue);font-weight:400}
.welcome-body{display:flex;gap:24px;margin-top:18px;height:240px}
.video{width:424px;height:230px;position:relative;background:linear-gradient(135deg,#3c5d9c,#8ea0b8 55%,#c8a09a)}
.video-bar{position:absolute;left:0;bottom:0;width:100%;height:22px;background:#111;display:flex;align-items:center;padding:0 8px;gap:8px}
.video-bar b{flex:1;height:4px;background:#555;position:relative}
.video-bar b::before{content:"";position:absolute;left:0;top:0;width:45%;height:4px;background:#ddd}
.play{position:absolute;left:172px;top:78px;width:70px;height:46px;background:rgba(0,0,0,.55);border-radius:6px}
.play::after{content:"";position:absolute;left:28px;top:13px;border-left:18px solid #fff;border-top:10px solid transparent;border-bottom:10px solid transparent}
.welcome-text{flex:1;font-size:12px;line-height:21px;color:#444}
.welcome-text .tags{margin-top:14px;font-size:13px;color:#333}
.btn-more{display:inline-block;margin-top:12px;background:var(--lime);color:var(--white);padding:7px 30px;font-size:13px}

/* cards */
.features{display:flex;gap:20px;margin-top:28px}
.feature{flex:1;background:var(--panel);padding:16px 18px;height:332px}
.feature .shot{height:166px}
.feature h3{font-family:"Raleway",sans-serif;font-weight:500;font-size:17px;margin:18px 0 10px;color:#222}
.feature p{font-size:11.5px;line-height:19px;color:#555;height:57px;overflow:hidden}
.feature .read{font-size:11.5px;color:#333;margin-top:10px;display:block}

/* accreditations */
.accred-head{display:flex;justify-content:space-between;align-items:center;margin-top:26px}
.accred-head h2{font-family:"Raleway",sans-serif;font-weight:300;font-size:29px;color:#444}
.accred-head h2 span{color:var(--blue);font-weight:400}
.arrows{display:flex;gap:6px}
.arrows i{width:17px;height:17px;border:1px solid #999;border-radius:50%}
.badges{display:flex;margin-top:12px;border:1px solid var(--line)}
.badges div{flex:1;height:54px;border-right:1px solid var(--line);display:flex;align-items:center;justify-content:center}
.badges div:last-child{border:0}
.badges span{width:120px;height:30px;background:#c9ccd2;border-radius:4px}

/* shop */
.shop{display:flex;gap:34px;margin-top:36px}
.shop-main{flex:1}
.shop-main h2{font-family:"Raleway",sans-serif;font-weight:400;font-size:25px;color:var(--blue)}
.shop-main h3{font-family:"Raleway",sans-serif;font-weight:400;font-size:17px;color:#333;margin-top:6px}
.shop-main .intro{font-size:11.5px;line-height:19px;margin-top:22px;color:#444}
.services{display:flex;gap:20px;margin-top:22px}
.services ul{list-style:none;flex:1}
.services li{font-size:11.5px;line-height:31px;color:#333;display:flex;align-items:center;gap:10px}
.services li::before{content:"";width:8px;height:1px;background:#555}

.booking{width:282px;border:1px solid var(--line);padding-bottom:14px}
.booking .head{background:var(--lime-soft);color:var(--white);font-family:"Raleway",sans-serif;font-size:23px;text-align:center;padding:12px 0}
.booking .offer{color:var(--red);font-size:15px;font-weight:600;line-height:19px;padding:14px 8px 0}
.booking .note{font-size:11.5px;color:#444;line-height:17px;padding:8px 8px 6px}
.field{margin:8px 8px 0;height:34px;border:1px solid #d6d6d6;font-size:11.5px;color:#888;display:flex;align-items:center;justify-content:space-between;padding:0 10px}
.row{display:flex;gap:6px;margin:8px 8px 0}
.row .field{margin:0;flex:1;justify-content:center}
.field.msg{height:34px}
.btn-schedule{margin:12px 8px 0;background:var(--blue-deep);color:var(--white);font-weight:700;font-size:17px;text-align:center;padding:12px 0}

/* owner */
.owner{margin-top:48px;background:#e2e8ef;height:202px;position:relative;padding:26px 22px}
.owner h2{font-family:"Raleway",sans-serif;font-weight:400;font-size:22px;color:#333}
.owner p{font-size:11.5px;line-height:19px;color:#444;width:690px;margin-top:12px}
.btn-consult{display:inline-block;margin-top:14px;background:var(--blue-deep);color:var(--white);font-size:12px;font-weight:600;padding:13px 20px;border:2px solid #0e3f8f}
.owner-portrait{position:absolute;right:18px;top:-40px;width:170px;height:242px;background:linear-gradient(180deg,#b8c4d4,#6f8fb8)}

/* actions */
.actions{display:flex;gap:24px;margin-top:38px}
.action{flex:1;height:58px;display:flex;align-items:center;background:var(--orange);color:var(--white);font-size:15px}
.action .ic{width:62px;height:58px;background:var(--orange-dark);display:flex;align-items:center;justify-content:center}
.action span{flex:1;text-align:center}

/* footer */
.site-footer{margin-top:28px;background:var(--footer);height:290px;padding:28px 20px;display:flex;gap:30px;color:var(--footer-text);font-size:11.5px}
.site-footer h4{color:var(--white);font-size:13px;font-weight:700;margin-bottom:22px}
.col-links{width:170px}.col-contact{width:230px}.col-feed{width:260px}.col-hours{flex:1}
.col-links li{list-style:none;line-height:22px}
.contact-line{display:flex;gap:10px;line-height:17px;margin-bottom:16px}
.feed p{line-height:16px}.feed small{display:block;margin:4px 0 12px}
.local-badge{width:80px;height:130px;background:#dfe3e8;margin-top:14px;border-radius:4px}
.copyright{background:var(--white);height:50px;display:flex;align-items:center;justify-content:space-between;padding:0 14px;font-size:11.5px;color:#444}
.social{display:flex;gap:18px}
.social i{width:14px;height:14px;border-radius:50%;background:#bbb}
</style>
</head>
<body>
<div class="page">
  <header class="site-header">
    <div class="header-photo" role="img" aria-label="Evening photo of the repair shop building"></div>
    <div class="owner-photo" role="img" aria-label="Portrait of the shop owner"></div>
    <div class="brand"><i class="dot"></i>Harbor Motor Repair</div>
    <div class="hours-card">
      <p><svg width="10" height="10" viewBox="0 0 10 10"><circle cx="5" cy="5" r="4" fill="none" stroke="#333"/><path d="M5 2v3h2" stroke="#333" fill="none"/></svg>Mon to Fri: 7am to 6 pm</p>
      <p><svg width="10" height="12" viewBox="0 0 10 12"><path d="M5 0a4 4 0 0 0-4 4c0 3 4 8 4 8s4-5 4-8a4 4 0 0 0-4-4z" fill="#333"/></svg>2210 S Harbor Ln Ste 4</p>
      <p style="padding-left:16px">Tempe, Arizona 85284</p>
    </div>
    <div class="call"><small>Call Us Today</small><strong>(480) 555-0142</strong></div>
    <div class="years-seal" role="img" aria-label="Years in business seal"></div>
  </header>

  <nav class="main-nav">
    <a class="current">HOME</a><a>ABOUT US</a><a>AUTO REPAIR SERVICES</a><a>CAR REPAIR COUPONS</a><a>OUR CUSTOMERS SPEAK</a><a>OUR BLOG</a><a>CONTACT US</a>
  </nav>

  <main class="content">
    <section class="hero" role="img" aria-label="Smiling technician working under the hood of a car">
      <div class="hero-caption">
        <h2>MSA Certified Technicians</h2>
        <p>Professional Mechanics Who Treat Your<br>Car As Their Own</p>
      </div>
      <div class="hero-dots"><i></i><i></i><i></i><i></i><i></i></div>
    </section>

    <section class="welcome">
      <h1>Welcome to <span>Harbor Motor Repair In Tempe</span></h1>
      <div class="welcome-body">
        <div class="video" role="img" aria-label="Video of a service advisor helping a customer at the counter">
          <div class="play"></div>
          <div class="video-bar"><svg width="8" height="10"><path d="M0 0l8 5-8 5z" fill="#ddd"/></svg><b></b></div>
        </div>
        <div class="welcome-text">
          <p>What sets our Tempe auto repair shop apart from the competition is our high level of competency as an automotive repair shop. When you need a car repair shop with qualified mechanics that can handle the toughest auto service and repair jobs, your search ends with us, whether you're in the Tempe, Chandler or Phoenix area. Our Tempe car repair center is a full service automotive repair shop with a strong track record in the performance of complex auto service and repair work. Many times these are services other auto repair shops tempe</p>
          <p class="tags">Auto Repair Tempe • Auto Repair Chandler • Auto Repair Phoenix</p>
          <span class="btn-more">View More</span>
        </div>
      </div>
    </section>

    <section class="features">
      <article class="feature">
        <div class="shot" role="img" aria-label="Advisor greeting a customer" style="background:linear-gradient(135deg,#5a7fb5,#c9b0a0)"></div>
        <h3>Family Owned and Operated</h3>
        <p>Harbor Motor Repair in Tempe AZ is a family owned and operated automotive repair shop that consistently receives positive</p>
        <span class="read">Read More »</span>
      </article>
      <article class="feature">
        <div class="shot" role="img" aria-label="Open engine bay of a car" style="background:linear-gradient(135deg,#2c2f3a,#7d8594)"></div>
        <h3>Going the Extra Mile</h3>
        <p>We also provide a courtesy shuttle service that will transport you to and pick you up from your home or office in Tempe, Chan-</p>
        <span class="read">Read More »</span>
      </article>
      <article class="feature">
        <div class="shot" role="img" aria-label="Mechanic holding tools beside a car" style="background:linear-gradient(135deg,#2f4f8a,#9fb0c8)"></div>
        <h3>Auto Service and Repair</h3>
        <p>We can fix that! That's more than a slogan, it's what we do everyday. Our Tempe auto repair shop is conveniently located at 2210</p>
        <span class="read">Read More »</span>
      </article>
    </section>

    <section class="accreditations">
      <div class="accred-head">
        <h2><span>Industry</span> Accreditations</h2>
        <div class="arrows"><i></i><i></i></div>
      </div>
      <div class="badges" role="img" aria-label="Industry partner badges">
        <div><span></span></div><div><span></span></div><div><span></span></div><div><span></span></div><div><span></span></div><div><span></span></div>
      </div>
    </section>

    <section class="shop">
      <div class="shop-main">
        <h2>Our Tempe Auto Repair Shop</h2>
        <h3>Offers the Following Automotive Services:</h3>
        <p class="intro">Harbor Motor Repair in Tempe is a top quality auto repair shop Phoenix area car owners have come to trust. We're located in south Tempe, just minutes from both Phoenix and Chandler.</p>
        <div class="services">
          <ul>
            <li>Shuttle Service</li><li>General Auto Repair &amp; Maintenance</li><li>Transmission Repair &amp; Replacement</li><li>Manufacturer Recommended Service</li><li>Brake Repair and Replacement</li><li>Air Conditioning A/C Repair</li><li>Tire Repair and Replacement</li><li>Fuel System Repair</li><li>Exhaust System Repair</li><li>Engine Cooling System Maintenance</li><li>Electrical Diagnostics</li><li>Steering and Suspension Work</li>
          </ul>
          <ul>
            <li>Starting and Charging Repair</li><li>Wheel Alignment</li><li>CV Axles</li><li>Computer Diagnostic Testing</li><li>Vehicle Preventative Maintenance</li><li>State Emissions Inspection</li><li>Emission Repair Facility</li><li>Tune Up</li><li>Oil Change</li><li>Brake Job / Brake Service</li><li>Engine Cooling System Flush &amp; Repair</li>
          </ul>
        </div>
      </div>
      <aside class="booking">
        <div class="head">Get Auto Repair</div>
        <p class="offer">Book Your Appointment Online Now And Get A $ 5 Discount!</p>
        <p class="note">Make an appointment now to have your car serviced properly, at the lowest possible price</p>
        <div class="field">Full Name<svg width="10" height="10"><circle cx="5" cy="3" r="3" fill="#bbb"/><rect x="0" y="7" width="10" height="3" fill="#bbb"/></svg></div>
        <div class="field">Email<svg width="12" height="9"><rect x=".5" y=".5" width="11" height="8" fill="none" stroke="#bbb"/></svg></div>
        <div class="field">Date</div>
        <div class="field">Select Time<svg width="9" height="9"><rect x=".5" y=".5" width="8" height="8" fill="none" stroke="#555"/><path d="M2 3l2.5 3L7 3z" fill="#555"/></svg></div>
        <div class="row"><div class="field">Year</div><div class="field">Make</div><div class="field">Model</div></div>
        <div class="field msg">Message</div>
        <div class="btn-schedule">SCHEDULE IT NOW</div>
      </aside>
    </section>

    <section class="owner">
      <h2>Get To Know Martin Kovacs, President of Harbor Motor Repair</h2>
      <p>Hello, I'm Martin Kovacs, President of Harbor Motor Repair. My team and I have been providing quality auto repair in Tempe, Arizona since 2001. We're a family owned, locally operated, business delivering honest and professional auto repair and car service to the people of Tempe, Chandler, Phoenix, Ahwatukee,</p>
      <span class="btn-consult">REQUEST A CONSULTATION</span>
      <div class="owner-portrait" role="img" aria-label="Portrait of the company president"></div>
    </section>

    <section class="actions">
      <div class="action"><div class="ic"><svg width="26" height="26" viewBox="0 0 26 26"><path d="M4 22l10-10M16 4a6 6 0 1 0 6 6l-4 0-2-2z" stroke="#fff" stroke-width="3" fill="none"/></svg></div><span>Track Your Repair</span></div>
      <div class="action"><div class="ic"><svg width="28" height="22" viewBox="0 0 28 22"><path d="M3 12l3-8h16l3 8v7H3z" fill="#fff"/><circle cx="8" cy="15" r="2" fill="#e58312"/><circle cx="20" cy="15" r="2" fill="#e58312"/></svg></div><span>Request A Loaner Vechicle</span></div>
      <div class="action"><div class="ic"><svg width="22" height="26" viewBox="0 0 22 26"><rect x="2" y="3" width="18" height="21" fill="none" stroke="#fff" stroke-width="2.5"/><path d="M6 10h10M6 15h10M6 20h6" stroke="#fff" stroke-width="2"/></svg></div><span>Make An Appointment</span></div>
    </section>

    <footer class="site-footer">
      <div class="col-links"><h4>OUR LINK</h4>
        <ul><li>Home</li><li>Auto Repair services</li><li>Car Repair Coupons</li><li>Our Customer Speak</li><li>Our Blog</li><li>Contact us</li></ul>
      </div>
      <div class="col-contact"><h4>CONTACT INFO</h4>
        <div class="contact-line"><svg width="10" height="12"><path d="M5 0a4 4 0 0 0-4 4c0 3 4 8 4 8s4-5 4-8a4 4 0 0 0-4-4z" fill="#9aa3b2"/></svg><span>Harbor Motor Repair<br>2210 S Harbor Ln Ste 4<br>Tempe, Arizona<br>85284 United States</span></div>
        <div class="contact-line"><svg width="12" height="9"><rect x=".5" y=".5" width="11" height="8" fill="none" stroke="#9aa3b2"/></svg><span>info@harbormotorrepairplace.com</span></div>
        <div class="contact-line"><svg width="10" height="12"><path d="M2 1h3l1 3-2 1a6 6 0 0 0 3 3l1-2 3 1v3c-6 1-10-4-9-9z" fill="#9aa3b2"/></svg><span>(480) 555-0187</span></div>
      </div>
      <div class="col-feed feed"><h4>LATEST FEEDLINE</h4>
        <p>@ Harbor news is simply fresh from the shop floor and our local team, posting service tips for</p><small>1 Day ago</small>
        <p>@ Fresh brake special this week only, ask our advisors</p><small>3 Day ago</small>
      </div>
      <div class="col-hours"><h4>WORKING HOURS</h4>
        <p>Mon to Fri: 7am to 6 pm<br>Sunday: Closed</p>
        <div class="local-badge" role="img" aria-label="Local business member badge"></div>
      </div>
    </footer>
    <div class="copyright">
      <span>Copyright © Harbor Motor Repair Tempe AZ 2014 All Rights Reserved. | Sitemap | Terms &amp; Conditions</span>
      <div class="social"><i></i><i></i><i></i><i></i><i></i></div>
    </div>
  </main>
</div>
</body>
</html>
```